Relaxation CD Cover

The relaxation cd is unique in that it does not include the typical windchimes, waterfalls, harps, etc. The feel is a mixture of jazz, spanish guitar, spiritual vibes and even some djembe drums. It includes mindfulness techniques that are used in yoga, meditation, and relaxation settings. The title right now is Gentle, Steady Unwinding. The cover should convey calm and cool with a bohemian and somewhat sultry feel. Maybe a bit afrocentric but not too much. A mock-up is attached, which includes a pic of the doctor who created the CD but the pic might be too sexy for the professional role. The color scheme especially the blue in the necklace is part of the branding so necessary to carry out. CD front and back should be consistent. Polish, modern, and clean can coexist with bohemian and relaxed. If you can do this then you've got the job! Please see both pics attached. The headshot is the desired pic to be included if artist does decide to use it but please do not feel limited to using the pics.
Updates

The pic does not have to be used in the pic...less literal please.

Target Market(s)

This CD will not only be marketed via Disc Nook and Tunebarn but also wellness stores, doc's offices;yoga retreats; local afrocentric fairs

Industry/Entity Type

Doctor

Requirements
Must have
• The color of the necklace or emphasize the necklace
Welcoming and relaxed feel (must be clear that this is a relaxation CD)
front and back must be consistent
A clear area where song titles will be located
Nice to have
• If the pic is included it should relate to the overall feel or color scheme...
Should not have
• -Bohemian does not mean messy or overly themed, e.g., too spanish or afrocentric

```html
<!DOCTYPE html>
<html lang="en">
<head>
<meta charset="utf-8">
<title>Gentle, Steady Unwinding — CD Cover</title>
<link href="https://fonts.googleapis.com/css2?family=Quicksand:wght@300;400&display=swap" rel="stylesheet">
<style>
  :root {
    --page-bg: #f3f3f3;
    --teal: #2fa9bf;
    --sea: #8fc7b4;
    --moss: #b9c46a;
    --sun: #e2b43c;
    --amber: #d9922c;
    --title-blue: #4db4ea;
    --title-ice: #cfeefc;
    --leaf: #3d8c3c;
    --leaf-light: #8dbb4a;
    --portrait-dark: #3a2a3a;
    --portrait-warm: #b98566;
    --white: #ffffff;
  }
  * { margin: 0; padding: 0; box-sizing: border-box; }
  html, body {
    width: 1200px;
    height: 922px;
    overflow: hidden;
    background: var(--page-bg);
  }
  .cover {
    position: absolute;
    left: 190px;
    top: 51px;
    width: 820px;
    height: 820px;
    overflow: hidden;
    background:
      radial-gradient(ellipse at 0% 0%, var(--teal) 0%, rgba(47,169,191,0) 45%),
      radial-gradient(ellipse at 100% 100%, var(--amber) 0%, rgba(217,146,44,0) 55%),
      linear-gradient(135deg, var(--sea) 0%, var(--moss) 45%, var(--sun) 80%);
    font-family: "Quicksand", sans-serif;
  }
  .subtitle {
    position: absolute;
    top: 96px;
    left: 0;
    width: 100%;
    text-align: center;
    font-weight: 300;
    font-size: 28px;
    letter-spacing: 2px;
    color: var(--white);
    opacity: 0.9;
  }
  .title {
    position: absolute;
    top: 118px;
    left: 0;
    width: 100%;
    text-align: center;
    font-weight: 300;
    font-size: 168px;
    line-height: 1;
    letter-spacing: 4px;
    background: linear-gradient(90deg, var(--title-ice) 0%, var(--title-blue) 40%, var(--title-blue) 70%, var(--title-ice) 100%);
    -webkit-background-clip: text;
    background-clip: text;
    color: transparent;
    z-index: 1;
  }
  .portrait {
    position: absolute;
    left: 232px;
    top: 230px;
    width: 360px;
    height: 520px;
    border-radius: 180px 180px 40px 40px;
    background: linear-gradient(180deg, var(--portrait-dark) 0%, var(--portrait-dark) 30%, var(--portrait-warm) 55%, var(--sea) 80%, var(--portrait-warm) 100%);
    z-index: 2;
  }
  .flora {
    position: absolute;
    left: 0;
    bottom: 0;
    width: 820px;
    height: 340px;
    z-index: 3;
  }
  .artist {
    position: absolute;
    bottom: 36px;
    left: 0;
    width: 100%;
    text-align: center;
    font-weight: 400;
    font-size: 28px;
    letter-spacing: 1px;
    color: var(--white);
    z-index: 4;
  }
</style>
</head>
<body>
  <section class="cover">
    <p class="subtitle">STEADY UNWINDING</p>
    <h1 class="title">GENTLE</h1>
    <div class="portrait" role="img" aria-label="Portrait photograph of the doctor with natural hair and a turquoise necklace"></div>
    <svg class="flora" viewBox="0 0 820 340" role="img" aria-label="Line-drawn illustration of leaves and blossoms in green and amber">
      <defs>
        <linearGradient id="floraFill" x1="0" y1="0" x2="1" y2="0">
          <stop offset="0" stop-color="#6fa84a" stop-opacity="0.75"/>
          <stop offset="0.5" stop-color="#3d8c3c" stop-opacity="0.9"/>
          <stop offset="1" stop-color="#d9922c" stop-opacity="0.85"/>
        </linearGradient>
      </defs>
      <path d="M0 110 Q120 60 240 130 Q330 90 410 140 Q520 40 640 90 Q740 60 820 120 L820 340 L0 340 Z" fill="url(#floraFill)"/>
    </svg>
    <p class="artist">DR. LENORA HAYE</p>
  </section>
</body>
</html>
```